IT Company needs Website for new Web and Mobile products for Sports and Fitness

Background:

We developed web based white label frontend web solution, backend services and white label mobile apps for to log, analyze, share and control sport and fitness activities. The name of this product suite is "Trelvano" (http://trelvano-example.com)

This products will be used by customers that provide platforms and community systems for sport and fitness. One of the major USP's is, that our technology i open for nearly all common formats, devices and apps out in the market. This means, you can just upload your data directly from device, file or app - e.G. Brindle, Vextor, Kalppi, StrideNook, Jogmelda, BipBop and much others.

Two current concrete examples/References

(1) MyOrvane
It's an international platform from orvane for runners. It provides individual training lans and a training log. MyOrvane uses the Backend Product "Trelvano Hub" (see http://hub.trelvano-example.net for a landing page) to integrate device, file and app support. Before this, every user has to track his training with manual inputs

(2) Paceharbor and qel-zine
Both are German customers. Paceharor is focused on runners. qel-zine is focused on Triatheletes. Both use the Product "Trelvano Web". This is a complete web solution with web based frontend solutions for athletes and coaches.

What do we need?
We need website layout for B2B for our products. We don't need lot's of pages. We need the pretty and nice layout, so we can derive the pages we need.

IMPORTANT
We don't talk about the webpages for the product itself (this will be a different project in future). We talk about a website, explaining the products)
Updates

Hi all,

we just start reviewing the first designs, and try to give feedback as detailed as possible. We attached a PDF document, to describe the the products a little bit more detailed. 

As written in the description, in the end we have two different sections. One is the usual stuff like "start page", "about", "contact", "disclaimer", "pricing", "blah...." and one will be the Developer Section, the "Tec Section". This ist aimed to developers (of our customers) that will integrate our products in there existing system or which will integrate our services in there own software.  This "pages" are more like "documentation", so easy to read and cool to look at (cause developers likes it cool, but straight)

Dear all,

we just do the final review. Cause this week is with heavy load, it takes some time...

Cheers

Ulrik

Target Market(s)

* Platforms and Communities for sport, health and fitness
* Gyms

Industry/Entity Type

Concrete

Font styles to use
Sans Serif

Requirements
Must have
• * Templates shall base on bootstrap. If not, it shall be easily realized on our site with bootstrap or out of the box "full responsive"

* HTML5 / CSS3
Nice to have
• PAGES
- Start Page
- Generic Template (from which we can derive additional pages)
- Contact Page
- Disclaimer Page
- Blog/News Page
- "About us" Page (can be combined with disclaimer)
- One Example product page (in end we have 3 products), shall show (if you need product details, let me know)
- product and it's description
- pricing information
- Add-Ons for the product
- Developer Section Page (Start Point for developers, where the finde "basic technical concepts and developer API's
- Example Developer Page for technical concept
- Example Developer Page for API

LOGO ISSUE
You can use an align to the Logo attached OR provide a new logo. The given logo is a logo for our own B2C Website http://trelvano-example.net. It's not really necessary, that the logo or the color must be used for the product website. Maybe it will be better if it's a complete new one, to avoid irritation between Trelvano as a B2B product and trelvano-example.net as a B2C platform.
Should not have
• No Flash and other proprietary technologies

```html
<!DOCTYPE html>
<html lang="en">
<head>
<meta charset="utf-8">
<title>Trelvano — Responsive Design</title>
<link rel="stylesheet" href="https://fonts.googleapis.com/css2?family=Open+Sans:wght@400;600;700&display=swap">
<style>
  :root {
    --brand-blue: #1a6fdf;
    --text-dark: #333a40;
    --text-body: #3c4248;
    --header-bg: #ffffff;
    --hero-bg-top: #f2f3f5;
    --hero-bg-bottom: #e6e8eb;
    --divider: #d4d7db;
    --menu-border: #ececec;
    --device-dark: #3a3d41;
    --device-light: #d9dbde;
  }
  * { box-sizing: border-box; margin: 0; padding: 0; }
  html, body {
    width: 1200px;
    height: 457px;
    overflow: hidden;
    font-family: "Open Sans", Arial, sans-serif;
    background: var(--hero-bg-top);
  }
  .page { position: relative; width: 1200px; height: 457px; overflow: hidden; }

  .site-header {
    position: absolute; inset: 0 0 auto 0; height: 70px;
    background: var(--header-bg);
    box-shadow: 0 1px 6px rgba(0,0,0,0.12);
    z-index: 3;
  }
  .brand {
    position: absolute; left: 88px; top: 14px;
    display: flex; align-items: center; gap: 8px;
    font-size: 26px; font-weight: 700; color: var(--brand-blue);
    text-decoration: none; letter-spacing: 0.2px;
  }
  .brand-mark { width: 14px; height: 14px; background: var(--brand-blue); }

  .main-nav { position: absolute; top: 0; left: 0; height: 70px; }
  .main-nav a {
    position: absolute; top: 24px;
    font-size: 13px; font-weight: 600; color: var(--text-dark);
    text-decoration: none; white-space: nowrap;
  }
  .main-nav a.is-active { color: var(--brand-blue); }

  .hero {
    position: absolute; left: 0; top: 70px; width: 1200px; height: 387px;
    background: linear-gradient(180deg, var(--hero-bg-top), var(--hero-bg-bottom));
  }
  .hero-backdrop {
    position: absolute; inset: 0;
    background: linear-gradient(90deg, rgba(200,203,208,0.55) 0%, rgba(236,238,241,0.2) 40%, rgba(210,213,218,0.45) 100%);
  }
  .hero-kicker {
    position: absolute; left: 93px; top: 74px;
    font-size: 20px; font-weight: 400; color: var(--text-dark);
  }
  .hero-title {
    position: absolute; left: 93px; top: 98px;
    font-size: 50px; font-weight: 700; color: var(--brand-blue);
    letter-spacing: 0.5px; white-space: nowrap;
  }
  .hero-divider {
    position: absolute; left: 93px; width: 507px; height: 1px;
    background: var(--divider);
  }
  .hero-copy {
    position: absolute; left: 93px; top: 206px; width: 505px;
    font-size: 14.5px; line-height: 24px; color: var(--text-body);
  }
  .cta-button {
    position: absolute; left: 93px; top: 327px; width: 170px; height: 42px;
    border: 1px solid var(--brand-blue); border-radius: 2px;
    display: flex; align-items: center; justify-content: center; gap: 9px;
    font-size: 16px; color: var(--brand-blue); text-decoration: none;
  }

  .device-showcase {
    position: absolute; left: 617px; top: 70px; width: 512px; height: 300px;
    background: linear-gradient(160deg, var(--device-light) 0%, #b9bcc0 45%, var(--device-dark) 100%);
    border-radius: 10px;
    opacity: 0.85;
  }

  .dropdown-menu {
    position: absolute; left: 843px; top: 62px; width: 168px;
    background: #fff; list-style: none;
    box-shadow: 0 2px 8px rgba(0,0,0,0.14);
    z-index: 4;
  }
  .dropdown-menu li {
    height: 36px; padding-left: 15px;
    display: flex; align-items: center;
    font-size: 11px; color: var(--text-dark);
    border-bottom: 1px solid var(--menu-border);
    letter-spacing: 0.2px;
  }
  .dropdown-menu li:last-child { border-bottom: none; }
  .dropdown-menu li.is-active { background: var(--brand-blue); color: #fff; }
</style>
</head>
<body>
<div class="page">
  <header class="site-header">
    <a class="brand" href="#"><span class="brand-mark"></span>Trelvano</a>
    <nav class="main-nav">
      <a class="is-active" href="#" style="left:633px">HOME</a>
      <a href="#" style="left:701px">PAGES</a>
      <a href="#" style="left:770px">FEATURES</a>
      <a href="#" style="left:858px">PORTFOLIO</a>
      <a href="#" style="left:957px">BLOG</a>
      <a href="#" style="left:1022px">CONTACT</a>
    </nav>
  </header>

  <ul class="dropdown-menu">
    <li>SINGLE IMAGE</li>
    <li>2 COLUMNS</li>
    <li>3 COLUMNS</li>
    <li>4 COLUMNS</li>
    <li class="is-active">PORTFOLIO + SIDEBAR</li>
    <li>PORTFOLIO FANCY</li>
  </ul>

  <section class="hero">
    <div class="hero-backdrop" role="img" aria-label="Faded city skyline photograph in light grey tones"></div>
    <p class="hero-kicker">Desktop Tablet and Mobile Friendly</p>
    <h1 class="hero-title">RESPONSIVE DESIGN</h1>
    <div class="hero-divider" style="top:185px"></div>
    <p class="hero-copy">Many desktop publishing packages and web page editors now use the lorem Ipsum as their default model text, and a search for 'lorem ipsum will uncover many web sites still in their infancy.</p>
    <div class="hero-divider" style="top:297px"></div>
    <a class="cta-button" href="#">
      <svg width="14" height="14" viewBox="0 0 14 14" aria-hidden="true"><path d="M13 1 L1 6.2 L6.3 7.7 L7.8 13 Z" fill="var(--brand-blue)"/></svg>
      GET STARTED
    </a>
    <div class="device-showcase" role="img" aria-label="Illustration of a desktop monitor, laptop, tablet and smartphone showing responsive screens"></div>
  </section>
</div>
</body>
</html>
```